strength and conditioning business needs a brochure

We are after a simple yet bold brochure design that uses base colours of red, white, black and grey. We have supporting text that we would like incorporated to see how it all looks as a finished product, as well as the logo.
Reason: To give designers a last chance to make recommended changes before choice is made.
Business

```html
<!DOCTYPE html>
<html lang="en">
<head>
<meta charset="utf-8">
<title>Core Build Fitness – Brochure</title>
<link rel="stylesheet" href="https://fonts.googleapis.com/css2?family=Exo:wght@400;800&family=Saira:wdth,wght@125,400;125,500;125,600;125,700&display=swap">
<style>
  :root {
    --red: #d71f27;
    --red-bright: #e4262f;
    --red-dark: #b3151c;
    --black: #0d0d0d;
    --charcoal: #262626;
    --grey: #cfcfcf;
    --light: #f1f1f1;
    --white: #ffffff;
    --text: #222222;
    --brand-grey: #3a3a3a;
  }
  * { margin: 0; padding: 0; box-sizing: border-box; }
  html, body { width: 1200px; height: 929px; overflow: hidden; background: var(--white); }
  .brochure { position: relative; width: 1200px; height: 929px; font-family: "Exo", sans-serif; }
  .panel { position: absolute; top: 0; width: 400px; height: 929px; overflow: hidden; }
  .panel--join { left: 0; background: linear-gradient(180deg, var(--white) 320px, #f4f4f4 560px, #e9e9e9 760px, #f6f6f6 929px); }
  .panel--cover-a { left: 400px; }
  .panel--cover-b { left: 800px; }

  .photo { position: absolute; left: 0; top: 0; width: 400px; }
  .photo--arm {
    height: 240px;
    background:
      radial-gradient(ellipse 70% 45% at 60% 75%, rgba(190,190,190,.85) 0%, rgba(120,120,120,.55) 40%, rgba(0,0,0,0) 75%),
      radial-gradient(ellipse 25% 30% at 52% 22%, rgba(170,170,170,.7) 0%, rgba(0,0,0,0) 80%),
      radial-gradient(ellipse 20% 60% at 4% 40%, rgba(150,150,150,.6) 0%, rgba(0,0,0,0) 80%),
      var(--black);
  }
  .photo--athlete {
    height: 405px;
    background:
      radial-gradient(ellipse 35% 30% at 74% 40%, rgba(215,31,39,.35) 0%, rgba(215,31,39,0) 80%),
      radial-gradient(ellipse 40% 25% at 30% 8%, rgba(215,60,60,.28) 0%, rgba(0,0,0,0) 80%),
      radial-gradient(ellipse 38% 50% at 36% 45%, rgba(185,185,185,.9) 0%, rgba(110,110,110,.6) 45%, rgba(0,0,0,0) 80%),
      radial-gradient(ellipse 25% 22% at 85% 85%, rgba(220,80,80,.35) 0%, rgba(0,0,0,0) 80%),
      var(--black);
  }
  .photo--athlete-b {
    height: 405px;
    background:
      radial-gradient(ellipse 45% 35% at 30% 30%, rgba(220,90,70,.32) 0%, rgba(0,0,0,0) 80%),
      radial-gradient(ellipse 30% 30% at 88% 20%, rgba(220,90,70,.25) 0%, rgba(0,0,0,0) 80%),
      radial-gradient(ellipse 40% 45% at 50% 55%, rgba(175,175,175,.85) 0%, rgba(95,95,95,.55) 45%, rgba(0,0,0,0) 80%),
      linear-gradient(180deg, #2a2a2a 0%, #151515 100%);
  }

  .join-banner { position: absolute; left: 0; top: 240px; width: 400px; height: 62px; }
  .join-banner h2 { position: absolute; left: 20px; top: 11px; color: var(--white); font-family: "Saira", sans-serif; font-stretch: 125%; font-weight: 500; font-size: 30px; letter-spacing: 1px; }
  .join-rule { position: absolute; left: 0; top: 313px; width: 400px; height: 7px; background: var(--red); }

  .join-copy { position: absolute; left: 22px; top: 340px; width: 355px; font-size: 14.5px; line-height: 1.4; color: var(--text); }
  .join-copy p + p { margin-top: 19px; }

  .contact-box { position: absolute; left: 0; top: 505px; width: 380px; height: 208px; }
  .contact-icon { position: absolute; left: 22px; top: 523px; }
  .contact-email { position: absolute; left: 22px; top: 630px; color: var(--white); font-family: "Saira", sans-serif; font-stretch: 125%; font-size: 26px; line-height: 1.2; letter-spacing: 0.2px; }
  .contact-email strong { font-weight: 600; display: block; }
  .contact-email span { font-weight: 400; }

  .brand { position: absolute; font-family: "Exo", sans-serif; font-weight: 800; color: var(--brand-grey); text-transform: uppercase; letter-spacing: 1.5px; display: flex; align-items: center; gap: 12px; white-space: nowrap; }
  .brand .mark { width: 16px; height: 16px; background: var(--red); flex: none; }
  .brand--footer { left: 24px; top: 856px; font-size: 28px; }
  .join-footer-strip { position: absolute; left: 0; bottom: 0; width: 400px; height: 14px; background: var(--red); }

  .brand-plate { position: absolute; left: 0; top: 323px; width: 400px; height: 72px; }
  .brand--plate { left: 22px; top: 341px; font-size: 25px; }

  .grey-band { position: absolute; left: 0; top: 405px; width: 400px; height: 13px; background: linear-gradient(180deg, #dadada, #c4c4c4); }
  .red-field {
    position: absolute; left: 0; top: 418px; width: 400px; height: 511px;
    background:
      radial-gradient(ellipse 30% 55% at 20% 30%, rgba(255,120,120,.16) 0%, rgba(255,120,120,0) 80%),
      radial-gradient(ellipse 25% 45% at 80% 55%, rgba(255,120,120,.13) 0%, rgba(255,120,120,0) 80%),
      radial-gradient(ellipse 40% 30% at 50% 90%, rgba(120,0,0,.18) 0%, rgba(120,0,0,0) 80%),
      linear-gradient(160deg, var(--red-bright) 0%, var(--red) 55%, var(--red-dark) 100%);
  }
  .tagline { position: absolute; left: 22px; top: 870px; width: 358px; color: var(--white); font-family: "Saira", sans-serif; font-stretch: 125%; font-weight: 600; font-size: 25px; letter-spacing: 0; padding-bottom: 4px; border-bottom: 2px solid var(--white); white-space: nowrap; }
  .tagline em { font-style: normal; font-weight: 400; }
</style>
</head>
<body>
<main class="brochure">

  <section class="panel panel--join">
    <div class="photo photo--arm" role="img" aria-label="Black and white photo of an athlete flexing her arm"></div>
    <svg class="join-banner" viewBox="0 0 400 62" aria-hidden="true">
      <polygon points="0,0 300,0 333,62 0,62" fill="var(--red)"/>
    </svg>
    <div class="join-banner"><h2>HOW TO JOIN?</h2></div>
    <div class="join-rule"></div>

    <div class="join-copy">
      <p>CBF is a subscription-based resource but you are not locked in to any contracts. In fact, at any time you want you can cancel your subscription, no questions asked.</p>
      <p>To join, send us an email to the address below and we will walk you through the very simple steps to join:</p>
    </div>

    <svg class="contact-box" viewBox="0 0 380 208" aria-hidden="true">
      <polygon points="-2,2 352,2 378,28 378,180 352,206 -2,206" fill="var(--charcoal)" stroke="var(--red)" stroke-width="2.5"/>
    </svg>
    <svg class="contact-icon" width="94" height="94" viewBox="0 0 94 94" aria-hidden="true">
      <circle cx="47" cy="47" r="44" fill="var(--red)"/>
      <circle cx="47" cy="47" r="39" fill="none" stroke="var(--charcoal)" stroke-width="2.5"/>
      <rect x="24" y="31" width="46" height="32" fill="none" stroke="var(--black)" stroke-width="3"/>
      <polyline points="24,31 47,50 70,31" fill="none" stroke="var(--black)" stroke-width="3"/>
      <line x1="24" y1="63" x2="40" y2="45" stroke="var(--black)" stroke-width="2.5"/>
      <line x1="70" y1="63" x2="54" y2="45" stroke="var(--black)" stroke-width="2.5"/>
    </svg>
    <p class="contact-email"><strong>CoreBuildFitness</strong><span>@mailhub.com</span></p>

    <div class="brand brand--footer"><span class="mark"></span>Core Build Fitness</div>
    <div class="join-footer-strip"></div>
  </section>

  <section class="panel panel--cover-a">
    <div class="photo photo--athlete" role="img" aria-label="Black and white photo of a muscular male athlete with red smoke swirls"></div>
    <svg class="brand-plate" viewBox="0 0 400 72" aria-hidden="true">
      <defs><linearGradient id="plateA" x1="0" y1="0" x2="0" y2="1"><stop offset="0" stop-color="#ffffff"/><stop offset="1" stop-color="#d8d8d8"/></linearGradient></defs>
      <polygon points="0,0 310,0 350,72 0,72" fill="url(#plateA)"/>
    </svg>
    <div class="brand brand--plate"><span class="mark"></span>Core Build Fitness</div>
    <div class="grey-band"></div>
    <div class="red-field" role="img" aria-label="Red background with faint smoke texture"></div>
    <p class="tagline">KNOWLEDGE <em>IS</em> POWER</p>
  </section>

  <section class="panel panel--cover-b">
    <div class="photo photo--athlete-b" role="img" aria-label="Black and white photo of a female athlete resting with red smoke swirls"></div>
    <svg class="brand-plate" viewBox="0 0 400 72" aria-hidden="true">
      <defs><linearGradient id="plateB" x1="0" y1="0" x2="0" y2="1"><stop offset="0" stop-color="#ffffff"/><stop offset="1" stop-color="#d8d8d8"/></linearGradient></defs>
      <polygon points="0,0 310,0 350,72 0,72" fill="url(#plateB)"/>
    </svg>
    <div class="brand brand--plate"><span class="mark"></span>Core Build Fitness</div>
    <div class="grey-band"></div>
    <div class="red-field" role="img" aria-label="Red background with faint smoke texture"></div>
    <p class="tagline">KNOWLEDGE <em>IS</em> POWER</p>
  </section>

</main>
</body>
</html>
```